Office Stationary and Business Card package

I need a new fresh looking business card and stationary design. "I need to refresh and update my Stationary and Business card appearance.

We are a family dental practice that handles all phases of dentistry including cosmetic, emergency and implant restoration We like the use of Blue and Grey in the design. i would like to include my website address and Phone numbers on the new project as well as a choice of different back sides to business cards which might include a map, appointment information, or blank depending on the particular card. The business cards should allow for the inclusion of another persons name and title in some location.

Information to be included in stationery:

Gordon T Malvey DMD, FAIDS
A Professional Dental Corporation (this needs to be
somewhere on the stationary and business cards)
48160 Orchard Lane
Fairmont, CA 91458
PHONE: (555) 317-4092
WEBSITE: www.gordonmalveydmd.example

Designs need to be Vibrant, Professional and Clean.
Colors to use: Blue, Grey and White colors.

I currently do not have an existing logo. I would like something simply, similar to the attached.

```html
<!DOCTYPE html>
<html lang="en">
<head>
<meta charset="utf-8">
<title>Malvey Dental – Business Card</title>
<link rel="stylesheet" href="https://fonts.googleapis.com/css2?family=Sarabun:wght@300;400;500&display=swap">
<style>
  :root {
    --sky: #6cbde8;
    --sky-light: #8dcdf0;
    --sky-deep: #58afe0;
    --ink: #5d6166;
    --ink-soft: #7b8086;
    --paper: #f7f7f7;
    --stage: #dcdde0;
    --white: #ffffff;
  }
  * { box-sizing: border-box; margin: 0; padding: 0; }
  html, body {
    width: 1200px; height: 900px; overflow: hidden;
    background: var(--stage);
    font-family: "Sarabun", Arial, sans-serif;
    color: var(--ink);
  }
  .sheet {
    width: 1200px; height: 900px;
    display: flex; flex-direction: column;
    align-items: center; justify-content: center; gap: 60px;
  }
  .card {
    position: relative;
    width: 560px; height: 320px;
    overflow: hidden;
    box-shadow: 0 2px 10px rgba(0,0,0,0.08);
  }
  /* front */
  .card-front { background: var(--paper); }
  .card-front .edge-band {
    position: absolute; left: 0; right: 0; bottom: 0; height: 12px;
    background: var(--sky);
  }
  .brand-mark {
    position: absolute; top: 34px; right: 40px;
    display: flex; align-items: center; gap: 10px;
    font-size: 24px; font-weight: 500; color: var(--sky);
  }
  .brand-mark .dot {
    width: 16px; height: 16px; border-radius: 50%; background: var(--sky);
  }
  .corporation {
    position: absolute; left: 40px; top: 128px;
    font-size: 21px; font-weight: 300; color: var(--ink-soft);
    letter-spacing: 0.2px;
  }
  .contact {
    position: absolute; left: 40px; top: 186px;
    width: 272px;
  }
  .contact .name {
    font-size: 19px; font-weight: 500; color: var(--ink);
    white-space: nowrap;
  }
  .contact .name .credentials { color: var(--sky); font-weight: 400; }
  .contact .line {
    display: flex; justify-content: flex-end; align-items: center; gap: 8px;
    font-size: 14px; font-weight: 300; color: var(--ink-soft);
    margin-top: 2px; white-space: nowrap;
  }
  .contact .line svg { flex: none; }
  .divider {
    position: absolute; left: 330px; top: 186px;
    width: 1px; height: 84px; background: var(--sky);
  }
  .office {
    position: absolute; left: 350px; top: 186px;
    font-size: 14px; font-weight: 300; font-style: normal;
    color: var(--ink-soft); line-height: 1.35;
  }
  .office .office-title { font-size: 17px; font-weight: 400; color: var(--sky); margin-bottom: 2px; }

  /* back */
  .card-back {
    background: radial-gradient(ellipse at 40% 40%, var(--sky-light) 0%, var(--sky) 55%, var(--sky-deep) 100%);
    display: flex; flex-direction: column; align-items: center; justify-content: center;
    color: var(--white);
  }
  .card-back .texture { position: absolute; inset: 0; }
  .card-back .brand-mark-large {
    position: relative;
    display: flex; align-items: center; gap: 14px;
    font-size: 40px; font-weight: 500; color: var(--white);
  }
  .card-back .brand-mark-large .dot {
    width: 24px; height: 24px; border-radius: 50%; background: var(--white);
  }
  .card-back .website {
    position: relative; margin-top: 40px;
    font-size: 15px; font-weight: 300; letter-spacing: 1.2px; color: var(--white);
  }
</style>
</head>
<body>
<main class="sheet">
  <section class="card card-front" aria-label="Business card front">
    <div class="brand-mark"><span class="dot"></span>Malvey Dental</div>
    <p class="corporation">A Professional Dental Corporation</p>
    <div class="contact">
      <p class="name">Gordon T Malvey <span class="credentials">DMD, FAIDS</span></p>
      <p class="line">(555) 317-4092
        <svg width="10" height="15" viewBox="0 0 10 15" aria-hidden="true"><rect x="1" y="0.75" width="8" height="13.5" rx="1.5" fill="none" stroke="#6cbde8" stroke-width="1.3"/><line x1="4" y1="11.5" x2="6" y2="11.5" stroke="#6cbde8" stroke-width="1.3"/></svg>
      </p>
      <p class="line">gmalvey@gordonmalveydmd.example
        <svg width="15" height="11" viewBox="0 0 15 11" aria-hidden="true"><rect x="0.75" y="0.75" width="13.5" height="9.5" fill="none" stroke="#6cbde8" stroke-width="1.3"/><polyline points="0.75,0.75 7.5,6 14.25,0.75" fill="none" stroke="#6cbde8" stroke-width="1.3"/></svg>
      </p>
    </div>
    <div class="divider"></div>
    <address class="office">
      <p class="office-title">Dr. Malvey's office</p>
      <p>48160 Orchard Lane</p>
      <p>Fairmont, CA 91458</p>
    </address>
    <div class="edge-band"></div>
  </section>

  <section class="card card-back" aria-label="Business card back">
    <div class="texture" role="img" aria-label="Soft pale blue bubble texture across the card back"></div>
    <div class="brand-mark-large"><span class="dot"></span>Malvey Dental</div>
    <p class="website">www.gordonmalveydmd.example</p>
  </section>
</main>
</body>
</html>
```